Business Card Design Project

I need a business card designed for FableHarbor, a website which has people share their fictional story ideas with others. The business cards should incorporate the websites's logo, which can be found at www.fableharbor-example.com .

Target Market(s)

These will be primarily used in business development activities, not given to customers. It therefore needs to have a clean, professional appearance, and yet communicate what the company is trying to achieve as a bold startup.

Industry/Entity Type

Business

```html
<!DOCTYPE html>
<html lang="en">
<head>
<meta charset="utf-8">
<title>FableHarbor Business Card</title>
<link rel="stylesheet" href="https://fonts.googleapis.com/css2?family=Open+Sans:wght@400;600&display=swap">
<style>
  :root {
    --navy: #1f4468;
    --navy-deep: #173653;
    --band: #ffffff;
    --ink: #1f4468;
    --icon-ring: #3a3f6b;
    --muted: #3f6080;
    --page: #ffffff;
    --text-light: #ffffff;
  }
  * { margin: 0; padding: 0; box-sizing: border-box; }
  html, body {
    width: 1013px;
    height: 1200px;
    overflow: hidden;
    background: var(--page);
    font-family: "Open Sans", Arial, sans-serif;
  }
  .card {
    position: absolute;
    left: 15px;
    width: 979px;
    background: var(--navy);
    box-shadow: 0 3px 9px rgba(0, 0, 0, 0.55);
    overflow: hidden;
  }
  .card--front { top: 15px; height: 561px; }
  .card--back { top: 623px; height: 559px; }

  .brand {
    position: absolute;
    color: var(--text-light);
    font-weight: 600;
    font-size: 80px;
    line-height: 1;
    letter-spacing: 0.5px;
  }
  .card--front .brand { left: 19px; top: 62px; }
  .card--back .brand { left: 0; right: 0; top: 30px; text-align: center; }

  .band {
    position: absolute;
    left: 0;
    width: 100%;
    background: var(--band);
  }
  .card--front .band { top: 191px; height: 117px; }
  .card--back .band { top: 133px; height: 88px; }

  .holder-name {
    position: absolute;
    left: 19px;
    top: 243px;
    font-size: 54px;
    font-weight: 400;
    line-height: 1;
    letter-spacing: 4px;
    color: var(--ink);
  }

  .actions {
    position: absolute;
    top: 144px;
    left: 617px;
    display: flex;
    gap: 12px;
  }
  .action {
    width: 106px;
    height: 106px;
    border-radius: 50%;
    background: var(--band);
    border: 2px solid var(--icon-ring);
    display: flex;
    align-items: center;
    justify-content: center;
  }
  .action svg { width: 50px; height: 50px; }

  .contact {
    position: absolute;
    right: 34px;
    color: var(--text-light);
    font-size: 24px;
    line-height: 1;
    letter-spacing: 0.6px;
    white-space: nowrap;
    text-align: right;
  }
  .contact--phones { top: 465px; right: 42px; }
  .contact--web { top: 505px; }
  .contact span + span { margin-left: 24px; }

  .site-url {
    position: absolute;
    left: 0; right: 0;
    top: 152px;
    text-align: center;
    font-size: 38px;
    letter-spacing: 2px;
    color: var(--ink);
  }

  .typewriter-scene {
    position: absolute;
    left: 0; top: 221px;
    width: 100%; height: 338px;
    background:
      radial-gradient(ellipse 55% 45% at 50% 40%, rgba(120, 150, 180, 0.45), rgba(31, 68, 104, 0) 70%),
      linear-gradient(180deg, #4a6a8c 0%, #2c5073 40%, var(--navy-deep) 100%);
  }

  .tagline {
    position: absolute;
    left: 0; right: 0;
    top: 480px;
    text-align: center;
    font-size: 46px;
    letter-spacing: 4px;
    color: var(--muted);
    white-space: nowrap;
  }
</style>
</head>
<body>

<section class="card card--front">
  <div class="brand">FableHarbor</div>
  <div class="band"></div>
  <h1 class="holder-name">First &amp; Last Name</h1>

  <div class="actions">
    <div class="action" aria-label="Write">
      <svg viewBox="0 0 50 50" fill="none" stroke="#1f4468" stroke-width="4" stroke-linejoin="round" stroke-linecap="round">
        <path d="M22 12H8v30h30V28"/>
        <path d="M18 33l4-10 18-18 6 6-18 18z" fill="#1f4468"/>
      </svg>
    </div>
    <div class="action" aria-label="Discuss">
      <svg viewBox="0 0 50 50" fill="none" stroke="#1f4468" stroke-width="3.5" stroke-linejoin="round">
        <path d="M6 10h26v16H18l-7 6v-6H6z"/>
        <path d="M36 18h8v16h-5v6l-7-6H22v-4"/>
      </svg>
    </div>
    <div class="action" aria-label="Favourite">
      <svg viewBox="0 0 50 50" fill="none" stroke="#1f4468" stroke-width="3.5" stroke-linejoin="round">
        <path d="M25 5l6 13 14 1.5-10.5 9.5 3 14L25 36l-12.5 7 3-14L5 19.5 19 18z"/>
      </svg>
    </div>
  </div>

  <p class="contact contact--phones">
    <span>Tel: 01632 960418</span><span>Cell: 01632 960418</span><span>Fax: 01632 960418</span>
  </p>
  <p class="contact contact--web">
    <span>Email: hello@fableharbor-example.com</span><span>www.fableharbor-example.com</span>
  </p>
</section>

<section class="card card--back">
  <div class="brand">FableHarbor</div>
  <div class="band"></div>
  <p class="site-url">www.fableharbor-example.com</p>
  <div class="typewriter-scene" role="img" aria-label="Faded close-up photograph of vintage typewriter keys"></div>
  <p class="tagline">Unleash the fiction writer in you</p>
</section>

</body>
</html>
```